Flyer-Design für Seniorenbetreuung
Zielgruppe
Wir sind eine Genossenschaft, welche ihren Immobilienbestand gern erweitern möchte. Dafür soll für unsere Partnerfirma (welche im Seniorenbetreuungssektor tätig ist) eine Flyer erdacht werden, welcher Senioren bzw. ihre Angehörigen anspricht die Wohneigentum besitzen. Viele Senioren besitzen Ein-, Mehrfamilienhäuser oder Eigentumswohnungen und können oder wollen diese nicht weiter vererben. Zusätzlich sind sie durch die Kosten des Eigentums, wie Steuern oder Instandhaltungskosten belastet. Unsere Genossenschaft bietet eine Lösung des Problems. Eine Übernahme des Eigentums bei gleichzeitigem lebenslangem Wohnrecht. Die Zielgruppe soll in dem Flyer auf die bestehende Probleme angesprochen werden und gleichzeitig eine individuelle Lösung angeboten werden, welche eine Mitgliedschaft in dem sozialen Verbund der Genossenschaft ist.
Aufgabenstellung
Der Designer hat hier völlig freie Hand. Es sollte auf die Zielgruppe passen.
Passende Texte soll sich der Designer selbst erdenken.
Nachtrag: Ich habe mittlerweile viele Zuschriften bekommen, dass die Aufgabenstellung sich Texte auszudenken etwas zu allgemein gefasst ist, daher versuche ich hier nochmal etwas Licht in Dunkle zu bringen. Ich habe genauso wenig eine Idee, wie und mit welcher Wortwahl ein Senior auf einfühlsame Weise darauf angesprochen werden soll, ob er nicht sein Haus verkaufen möchte. Meine bisherigen Ideen waren:
'Haben sie schon einmal über den Verkauf ihrer Immobilie nachgedacht? Wussten sie, dass sie ihr Wohneigentum im vollen Umfang weiter nutzen können, ohne weiter die Kosten tragen zu müssen? Sie wollen wissen wie? Rufen sie doch einfach an und ich werde ihnen genau erklären, welche Vorzüge die Mitgliedschaft in einer Genossenschaft mit sich bringt.'
Allerdings erscheint mir das viel zu direkt und ich finde nicht die richtigen Worte diese Personengruppe in dem Maße anzusprechen, wie es nötig wäre, um sie zu einem Anruf zu bewegen. Daher hatte ich gehofft, dass sie hier ein findiger Designer findet, welcher eine bessere kreative Art hat als ich.
Vielleicht ist es die falsche Plattform, vielleicht schaffen wir es nicht die Vorgaben zu spezifizieren. Bilder anzuordnen ist sicher sehr wichtig, auch ist es wichtig aufhellende Elemente einzubringen. Aber wir suchen jemanden der einen Flyer so gestalten kann das der Flyer etwas ausdrückt, das eine Botschaft vermittelt wird, das auf einem Blick der Senior den Wunsch verspürt, bei uns anzurufen. Das heißt viel wichtiger als Bilder, ist der Inhalt der Ansprache. Nicht unbedingt der Inhalt, sondern das WIE. Nochmal: wir wollen ältere Menschen dazu bewegen ihr Eigentum auf Grund von Reperaturrückstau, Überlastung, gesundheitlichen Einschränkungen, finanziellen Schwierigkeiten, zu großem Aufwand in eine Genossenschaft einzubringen. Ds heißt S..

```html
<!DOCTYPE html>
<html lang="de">
<head>
<meta charset="utf-8">
<title>Flyer Seniorenhilfe Wohnwert</title>
<link href="https://fonts.googleapis.com/css2?family=Russo+One&family=Lato:wght@300;400;700&family=Oswald:wght@400;500&family=Alegreya+Sans+SC:wght@500&display=swap" rel="stylesheet">
<style>
  :root {
    --backdrop: #e4e2de;
    --header-band: rgba(20, 50, 110, 0.75);
    --footer-band: #070c38;
    --edge-line: rgba(120, 190, 230, 0.55);
    --gold: #e2bd3f;
    --gold-deep: #b8922a;
    --white: #ffffff;
    --text-soft: #e3f1f6;
    --photo-dark: #2a2622;
  }
  * { margin: 0; padding: 0; box-sizing: border-box; }
  html, body { width: 1200px; height: 900px; overflow: hidden; background: var(--backdrop); }

  .flyer {
    position: absolute;
    left: 296px; top: 20px;
    width: 608px; height: 860px;
    overflow: hidden;
    box-shadow: 0 8px 24px rgba(0,0,0,0.25);
    background: var(--photo-dark);
  }
  .flyer-shapes { position: absolute; inset: 0; width: 100%; height: 100%; }

  .brand {
    position: absolute; right: 28px; top: 92px;
    text-align: right;
    font-family: "Russo One", sans-serif;
    text-transform: uppercase;
  }
  .brand-name { color: var(--gold); font-size: 20px; letter-spacing: 0.5px; }
  .brand-tagline { color: var(--white); font-size: 16px; margin-top: 4px; letter-spacing: 0.3px; }

  .headline {
    position: absolute; right: 28px; top: 204px;
    width: 320px; text-align: right;
    font-family: "Lato", sans-serif; font-weight: 700;
    color: var(--white); line-height: 1.22;
  }
  .headline-lead { display: block; font-size: 33px; margin-bottom: 2px; }
  .headline-rest { display: block; font-size: 24px; }

  .intro {
    position: absolute; right: 28px; top: 362px;
    width: 280px; text-align: right;
    font-family: "Lato", sans-serif; font-weight: 300;
    font-size: 18px; line-height: 1.55; color: var(--text-soft);
  }

  .seal {
    position: absolute; left: 290px; top: 500px;
    width: 96px; height: 96px; border-radius: 50%;
    background: radial-gradient(circle at 40% 35%, #f2d35a, var(--gold-deep));
    border: 5px solid rgba(110, 95, 40, 0.75);
  }

  .callout {
    position: absolute; right: 18px; top: 606px;
    width: 262px; text-align: right;
    font-family: "Lato", sans-serif;
  }
  .callout-title { color: var(--gold); font-weight: 700; font-size: 19px; text-transform: uppercase; letter-spacing: -0.2px; }
  .callout-text { color: var(--text-soft); font-size: 13px; line-height: 1.5; margin-top: 6px; font-weight: 400; }

  .contacts {
    position: absolute; left: 350px; right: 14px; top: 762px;
    display: flex; justify-content: space-between; align-items: flex-end;
    color: var(--gold);
  }
  .contact { display: flex; align-items: flex-end; gap: 6px; }
  .contact-icon { width: 20px; height: 30px; flex: none; }
  .contact-dot { width: 20px; height: 20px; border: 2px solid var(--gold); border-radius: 50%; flex: none; margin-bottom: 3px; }
  .contact-label { font-family: "Alegreya Sans SC", sans-serif; font-size: 10px; letter-spacing: 0.3px; }
  .contact-number { font-family: "Oswald", sans-serif; font-size: 16px; line-height: 1.1; }
</style>
</head>
<body>
  <main class="flyer">
    <svg class="flyer-shapes" viewBox="0 0 608 860" preserveAspectRatio="none">
      <defs>
        <linearGradient id="photoTone" x1="0" y1="0" x2="1" y2="0">
          <stop offset="0" stop-color="#5c4634"/>
          <stop offset="0.22" stop-color="#2c2a26"/>
          <stop offset="0.5" stop-color="#cfd6da"/>
          <stop offset="0.8" stop-color="#f4f6f7"/>
        </linearGradient>
        <linearGradient id="panelTone" x1="0" y1="0" x2="0" y2="1">
          <stop offset="0" stop-color="#1b5fa0"/>
          <stop offset="0.5" stop-color="#17708e"/>
          <stop offset="1" stop-color="#1a8a7c"/>
        </linearGradient>
      </defs>
      <rect class="photo-area" role="img" aria-label="Foto: älterer Herr mit Gehstock blickt aus einem hellen Fenster" x="0" y="0" width="608" height="860" fill="url(#photoTone)"/>
      <path class="info-panel" d="M150 0 C 260 160 330 430 335 860 L 608 860 L 608 0 Z" fill="url(#panelTone)"/>
      <path class="panel-edge" d="M150 0 C 260 160 330 430 335 860" fill="none" stroke="var(--edge-line)" stroke-width="6"/>
      <path class="header-band" d="M222 78 L 608 78 L 608 178 L 270 178 C 258 142 242 108 222 78 Z" fill="var(--header-band)"/>
      <path class="highlight-strip" d="M322 700 L 608 700 L 608 728 L 326 728 Z" fill="#2a9a86" opacity="0.7"/>
      <path class="footer-band" d="M327 728 L 608 728 L 608 860 L 335 860 Z" fill="var(--footer-band)"/>
    </svg>

    <header class="brand">
      <div class="brand-name">Seniorenhilfe Wohnwert</div>
      <div class="brand-tagline">Begleitet Sie auf jedem Schritt</div>
    </header>

    <h1 class="headline">
      <span class="headline-lead">Unterstützung von</span>
      <span class="headline-rest">Senioren und ihren Familien bei der Liquidation von Vermögenswerten</span>
    </h1>

    <p class="intro">Dies gibt ihnen die Freiheit, ihre Angehörigen in eine sicherere und bequemere Lebenssituation zu bringen.</p>

    <div class="seal" aria-hidden="true"></div>

    <section class="callout">
      <h2 class="callout-title">Du willst wissen wie?</h2>
      <p class="callout-text">Rufen Sie mich einfach an und ich erkläre Ihnen genau, welche Vorteile es hat, Mitglied einer Genossenschaft zu sein.</p>
    </section>

    <footer class="contacts">
      <div class="contact">
        <svg class="contact-icon" viewBox="0 0 20 30" aria-hidden="true">
          <rect x="2" y="1" width="16" height="28" rx="3" fill="none" stroke="#e2bd3f" stroke-width="2"/>
          <line x1="2" y1="23" x2="18" y2="23" stroke="#e2bd3f" stroke-width="2"/>
        </svg>
        <div>
          <div class="contact-label">Rufen Sie uns an:</div>
          <div class="contact-number">(212) 555-0148</div>
        </div>
      </div>
      <div class="contact">
        <span class="contact-dot" aria-hidden="true"></span>
        <div>
          <div class="contact-label">Messenger:</div>
          <div class="contact-number">(212) 555-0148</div>
        </div>
      </div>
    </footer>
  </main>
</body>
</html>
```